Flyer-Design für Hausarztpraxis
Zielgruppe
Hausarztpraxis, Zielgruppe junge Patienten ...
Aufgabenstellung
Mein aktueller Flyer sollte modernisiert werden ... Texte können gern überarbeitet werden... Neue Fotos der Praxis werden noch gemacht. DH die Datei sollte so sein, dass ich die Fotos anpassen kann hinterher
Farbe gern in dem schönen Magenta wie das Logo
Aufbau des Flysers sollte ebenfalls optimiert werden.

```html
<!DOCTYPE html>
<html lang="de">
<head>
<meta charset="utf-8">
<title>Hausarztpraxis Flyer – Innenseite</title>
<link href="https://fonts.googleapis.com/css2?family=Source+Sans+3:wght@400;600;700&display=swap" rel="stylesheet">
<style>
  :root {
    --magenta: #ad2455;
    --magenta-dark: #951d47;
    --paper: #f3f2ee;
    --ink: #2c2b2b;
    --photo-light: #d9d7d1;
    --photo-dark: #8f8c86;
    --backdrop: #dcd8d2;
  }
  * { box-sizing: border-box; margin: 0; padding: 0; }
  html, body { width: 1200px; height: 960px; overflow: hidden; background: var(--backdrop); }
  body { font-family: "Source Sans 3", sans-serif; color: var(--ink); }
  .flyer {
    position: absolute; left: 60px; top: 70px;
    width: 1080px; height: 820px; display: flex;
    box-shadow: 0 10px 30px rgba(0,0,0,.15);
  }
  .panel { position: relative; width: 360px; height: 820px; background: var(--paper); overflow: hidden; }
  .panel + .panel { border-left: 1px solid #e2e0da; }
  .shape { position: absolute; inset: 0; width: 360px; height: 820px; }
  .content { position: absolute; left: 34px; right: 30px; }
  h2 { color: var(--magenta); font-weight: 700; font-size: 23px; letter-spacing: .3px; line-height: 1.1; }
  h3 { color: var(--magenta); font-weight: 700; font-size: 19px; margin: 18px 0 4px; }
  p { font-size: 13.5px; line-height: 1.35; }
  .justify { text-align: justify; }
  .hours { font-weight: 700; font-size: 16px; line-height: 1.25; margin: 10px 0; }
  .photo { position: absolute; }
  .bubble { position: absolute; }
  .bubble-text {
    position: absolute; color: var(--magenta); font-weight: 700;
    font-size: 13.5px; line-height: 1.15; text-align: center;
  }
  .doctor-band { position: absolute; left: 0; top: 600px; width: 360px; height: 110px; color: #fff; padding: 28px 26px 0; }
  .doctor-name { font-weight: 700; font-size: 17px; letter-spacing: .3px; }
  .doctor-info { font-size: 14px; line-height: 1.25; }
</style>
</head>
<body>
<main class="flyer">

  <!-- Panel 1: overview -->
  <section class="panel panel-overview">
    <svg class="shape" viewBox="0 0 360 820" aria-hidden="true">
      <defs>
        <linearGradient id="phoneArea" x1="0" y1="0" x2="1" y2="1">
          <stop offset="0" stop-color="#e6e4df"/><stop offset="1" stop-color="#c9c6c0"/>
        </linearGradient>
      </defs>
      <polygon points="0,780 360,800 360,820 0,820" fill="var(--magenta)"/>
    </svg>
    <svg class="photo" style="left:0;top:0" width="360" height="200" viewBox="0 0 360 200" role="img" aria-label="Foto: Telefonhörer auf hellem Hintergrund">
      <polygon points="0,0 360,0 360,200 0,130" fill="url(#phoneArea)"/>
    </svg>
    <div class="content" style="top:150px">
      <h2>UNSER ANGEBOT IM ÜBERBLICK</h2>
      <h3>Sprechstunden</h3>
      <p>Eine unserer sicher für Sie entscheidensten Veränderung sind unsere neuen Praxisöffnungszeiten.</p>
      <p class="hours">Mo 8-11:30 sowie 14-17 Uhr<br>Die 8-13 Uhr / Mi 8-13 Uhr<br>Do 8-11:30 sowie 14-18 Uhr<br>Fr 8-11:30</p>
      <p>Telefonisch erreichen Sie uns täglich von 8:00-11:00 Uhr sowie Montags und Donnerstags von 14:00-16:00 Uhr.</p>
      <h3>Laborzeiten</h3>
      <p class="justify">Unsere Laborzeiten sind nun vor der eigentlichen Sprechstunde von 7:15 -8:00 Uhr. Dazu kommt, dass Sie inzwischen die Möglichkeit haben, auch über unsere Website www.hausarzt-talbach.de, <strong>online Termine</strong> vereinbaren können.</p>
      <h3>Rezepte</h3>
      <p class="justify">Rezepte sollten ein Tag vor Abholung auf unsere Rezepthotline gesprochen werden, oder in den neuen Briefkasten im Hausflur eingeworfen werden. Diese werden dann nach der Sprechzeit für sie fertig-gestellt</p>
    </div>
  </section>

  <!-- Panel 2: news and photo -->
  <section class="panel panel-news">
    <svg class="shape" viewBox="0 0 360 820" aria-hidden="true">
      <polygon points="0,0 360,0 360,40 0,8" fill="var(--magenta)"/>
      <polygon points="0,8 360,40 360,46 0,14" fill="var(--paper)"/>
      <polygon points="0,812 360,800 360,820 0,820" fill="var(--magenta)"/>
    </svg>
    <div class="content" style="top:90px">
      <p class="justify">Wie Sie vielleicht feststellen konnten haben wir eine neue Praxissoftware und Hardware, um die Praxisabläufe zu optimieren und Ihnen kürzere Wartezeiten anbieten zu können. Über unseren TV im Wartezimmer sehen sie immer alle Neuigkeiten, wie Urlaube oder Kurse.</p>
    </div>
    <svg class="photo" style="left:0;top:300px" width="360" height="500" viewBox="0 0 360 500" role="img" aria-label="Foto: Behandlungsraum der Praxis mit Liege und Fenster">
      <defs>
        <linearGradient id="roomPhoto" x1="0" y1="0" x2="0" y2="1">
          <stop offset="0" stop-color="var(--photo-light)"/><stop offset="1" stop-color="var(--photo-dark)"/>
        </linearGradient>
      </defs>
      <rect x="0" y="40" width="360" height="460" fill="url(#roomPhoto)"/>
      <rect x="40" y="10" width="300" height="480" fill="none" stroke="var(--ink)" stroke-width="2"/>
    </svg>
    <svg class="bubble" style="left:140px;top:520px" width="200" height="150" viewBox="0 0 200 150" aria-hidden="true">
      <path d="M100,10 C160,8 192,40 188,72 C184,108 140,124 96,120 L52,140 L62,112 C24,102 8,80 12,58 C18,28 52,11 100,10 Z" fill="none" stroke="var(--magenta)" stroke-width="2.5"/>
    </svg>
    <div class="bubble-text" style="left:160px;top:545px;width:165px">Ich werde Sie mit Leidenschaft medizinisch betreuen und auch mit Herz für Ihre Probleme da sein!</div>
  </section>

  <!-- Panel 3: services and contact -->
  <section class="panel panel-services">
    <svg class="shape" viewBox="0 0 360 820" aria-hidden="true">
      <polygon points="0,790 360,805 360,820 0,820" fill="var(--magenta)"/>
    </svg>
    <div class="content" style="top:40px">
      <h3>Ultraschalluntersuchungen</h3>
      <p>Inzwischen können wir auch Ultraschalluntersuchungen der Schilddrüse, des Bauches sowie der Gefäße nach DUMED 2 Leitlinie anbieten.</p>
      <h3>Check-Ups</h3>
      <p class="justify">Es besteht auch die Möglichkeit außerhalb der kassenärztlichen Leistungen Check-UPs wahrzunehmen, wenn Sie es wünschen! Zum Beispiel ein erweiterter Frauen oder Männer Check.</p>
      <h3>Hyaloronsäure-Filler</h3>
      <p>Im Bereich der Ästhetik bieten wir Ihnen Hyaloronsäure-Filler im Gesicht zur Faltenenminimierung an.</p>
      <h3>Autogenes Training</h3>
      <p>Ebenfalls neu führen wir Einzel und Gruppenschulungen mit autogenem Training durch.</p>
    </div>
    <svg class="shape" style="top:600px;height:110px" width="360" height="110" viewBox="0 0 360 110" aria-hidden="true">
      <polygon points="0,0 360,14 360,110 0,96" fill="var(--magenta)"/>
    </svg>
    <div class="doctor-band">
      <div class="doctor-name">DR. MED. LENA WIESBRANDT</div>
      <div class="doctor-info">Fachärztin f. Allgemeinmedizin<br>Lindenweg 14 - 70999 Talbach</div>
    </div>
  </section>

</main>
</body>
</html>
```